Business Card Design

Hoping for a black background business card, minimalistic design.
With the Marble Crest logo you created in white.

I would like to include:
My Name and title
Address (street address)
Reception: (phone number)
Fax: (fax number)
Reception: (email address)
Direct email: (email address)
Instagram: (ig handle)

```html
<!DOCTYPE html>
<html lang="en">
<head>
<meta charset="utf-8">
<title>Marble Crest Business Card</title>
<link href="https://fonts.googleapis.com/css2?family=Poppins:wght@300;400;500;700&display=swap" rel="stylesheet">
<style>
  :root {
    --backdrop: #1a1a1a;
    --card: #1e1e1e;
    --card-edge: #2a2a2a;
    --ink: #ffffff;
    --ink-soft: #d6d6d6;
    --emboss: #262626;
    --emboss-line: #2e2e2e;
    --pattern-dark: #161616;
    --pattern-light: #3a3a3a;
  }
  * { margin: 0; padding: 0; box-sizing: border-box; }
  html, body {
    width: 1200px; height: 781px; overflow: hidden;
    background: var(--backdrop);
    font-family: "Poppins", sans-serif;
    color: var(--ink);
  }
  .canvas {
    width: 1200px; height: 781px;
    display: flex; align-items: center; justify-content: center; gap: 48px;
  }
  .card {
    position: relative;
    width: 540px; height: 309px;
    background: var(--card);
    border: 1px solid var(--card-edge);
    border-radius: 4px;
    overflow: hidden;
  }
  .brand {
    display: flex; align-items: center; gap: 10px;
    font-weight: 500; letter-spacing: 0.12em; text-transform: uppercase;
    color: var(--ink);
  }
  .brand-dot {
    border: 2px solid var(--ink); border-radius: 50%;
  }
  .card-front .brand { position: absolute; left: 34px; top: 30px; font-size: 17px; }
  .card-front .brand-dot { width: 34px; height: 34px; }
  .emboss-circle {
    position: absolute; right: 40px; top: 66px;
    width: 190px; height: 190px; border-radius: 50%;
    border: 2px solid var(--emboss-line);
    background: var(--emboss);
  }
  .contact {
    position: absolute; left: 34px; top: 118px;
    font-size: 11.5px; line-height: 1.45; color: var(--ink-soft);
  }
  .contact-name {
    font-size: 20px; font-weight: 700; letter-spacing: 0.06em;
    text-transform: uppercase; color: var(--ink); line-height: 1.1;
  }
  .contact-title { font-weight: 300; margin-bottom: 10px; }
  .contact-address { margin-bottom: 10px; }
  .contact-list { list-style: none; }
  .contact-list li { display: flex; align-items: center; gap: 7px; letter-spacing: 0.04em; }
  .contact-list svg { width: 11px; height: 11px; fill: var(--ink); flex: none; }
  .contact-list .at { width: 11px; font-size: 11px; text-align: center; color: var(--ink); }
  .card-back .pattern {
    position: absolute; inset: 0;
    background: linear-gradient(120deg, var(--pattern-dark) 0%, var(--card) 45%, var(--pattern-light) 100%);
  }
  .card-back .brand {
    position: absolute; left: 50%; top: 50%; transform: translate(-50%, -50%);
    font-size: 20px; white-space: nowrap;
  }
  .card-back .brand-dot { width: 38px; height: 38px; }
</style>
</head>
<body>
<main class="canvas">
  <section class="card card-front">
    <div class="brand"><span class="brand-dot"></span>Marble Crest</div>
    <div class="emboss-circle"></div>
    <div class="contact">
      <p class="contact-name">Owen Halloway</p>
      <p class="contact-title">C.O.O / Principal</p>
      <p class="contact-address">418 Linden Row,<br>Ottawa ON K2P 7B1</p>
      <ul class="contact-list">
        <li><svg viewBox="0 0 24 24"><path d="M3 8c3-4 15-4 18 0l-2 3-3-1V8H8v2l-3 1zM6 13h12l2 8H4z"/></svg>613-555-0142</li>
        <li><svg viewBox="0 0 24 24"><path d="M6 2l4 5-2 3c1 3 3 5 6 6l3-2 5 4-3 4C10 22 2 14 2 5z"/></svg>613-555-0187</li>
        <li><svg viewBox="0 0 24 24"><path d="M2 5h20v14H2zm2 2v1l8 5 8-5V7l-8 5z"/></svg>info@marblecresthg.com</li>
        <li><span class="at">@</span>@marblecresthg</li>
      </ul>
    </div>
  </section>
  <section class="card card-back">
    <div class="pattern" role="img" aria-label="Repeating embossed brand mark pattern in black with a glossy silver sheen toward the right"></div>
    <div class="brand"><span class="brand-dot"></span>Marble Crest</div>
  </section>
</main>
</body>
</html>
```